Law Firm Website

I currently have a temporary site that I created myself at www.mcorveyfirm.net (hosted by 9tree). I am generally happy with the content.

My permanent website just has basic information right now: www.mcorveyfirm.com (hosted by lumenrack). I want to take the general content from the temporary website and have a more professional looking website on the permanent website. I want it in Wordpress format. I want a link to my blog: www.crookedpath.com. I want it to work on pads and smart phones. My number and e-mail address should be available on every page. The idea is to feature the potential client more than the lawyer.
Updates

Several of the designs are good. I would like the front page to have my number and address at the top (and at the top of every page) and to identify my law firm as "Law Office of Gerald T. Corvey". No need to include "mcorveyfirm" as that is just the web address. I like showing the most recent blog posts on the front page. I don't need video. No need to emphasize office hours or map location on the front page (that could be under a contact button). My picture should be somewhere. I would like an image from Boston on the front page if we can find one that is not copyright protected. No images of gavels or scales of justice. See some of the sample websites I listed in previous messages. Thanks!

Industry/Entity Type

Law Firm

```html
<!DOCTYPE html>
<html lang="en">
<head>
<meta charset="utf-8">
<title>Law Office of Gerald T. Corvey</title>
<link rel="stylesheet" href="https://fonts.googleapis.com/css2?family=Nunito+Sans:wght@300;400;600&display=swap">
<style>
  :root {
    --cream: #f8f3e8;
    --white: #ffffff;
    --brown: #6f3d2c;
    --brown-light: #8a5441;
    --tab: #efe2c6;
    --text: #4b4540;
    --rule: #e8e0d0;
    --hero-rose: #efcfc9;
    --hero-sky: #cfe3ee;
  }
  * { margin: 0; padding: 0; box-sizing: border-box; }
  html, body { width: 922px; height: 1200px; overflow: hidden; }
  body {
    position: relative;
    background: var(--cream);
    font-family: "Nunito Sans", Arial, sans-serif;
    color: var(--text);
    font-size: 9.6px;
    line-height: 16px;
  }
  .abs { position: absolute; }
  h2 { font-weight: 400; font-size: 14.5px; color: var(--brown); letter-spacing: .3px; text-transform: uppercase; }
  .btn {
    position: absolute; display: inline-block; background: var(--brown); color: var(--white);
    font-size: 8.5px; letter-spacing: .3px; padding: 0 10px; height: 22px; line-height: 22px; text-decoration: none;
  }
  .link { color: var(--brown); font-size: 8.5px; text-decoration: none; }

  /* header */
  .brand { left: 57px; top: 22px; font-size: 26px; font-weight: 400; color: var(--brown); letter-spacing: .5px; line-height: 32px; }
  .brand b { font-weight: 400; color: #333; }
  .contact { top: 20px; font-size: 9px; line-height: 13px; color: var(--brown); }
  .contact .value { color: #333; }
  .contact.phone { left: 567px; padding-left: 21px; }
  .contact.phone .value { font-size: 17px; line-height: 22px; }
  .contact.email { left: 718px; padding-left: 22px; }
  .contact.email .value { font-size: 9.5px; line-height: 18px; }
  .contact svg { position: absolute; left: 0; top: 2px; }

  .nav { left: 0; top: 73px; width: 922px; height: 29px; background: var(--brown); }
  .nav ul { list-style: none; display: flex; margin-left: 56px; }
  .nav li { height: 29px; line-height: 29px; padding: 0 10.5px; color: var(--white); font-size: 9.6px; letter-spacing: .2px; }
  .nav li.active { background: var(--tab); color: var(--brown); padding: 0 14px; }

  /* hero */
  .hero { left: 57px; top: 105px; width: 808px; height: 289px; background: var(--white); padding: 3px; }
  .hero-art { width: 802px; height: 283px; background: linear-gradient(90deg, var(--hero-rose) 0%, #ecd3cf 45%, var(--hero-sky) 62%, #c99a6a 85%, #a66a36 100%); position: relative; }
  .hero-text { left: 27px; top: 75px; font-size: 21.5px; line-height: 25px; color: #3a2e2a; width: 420px; }
  .dots { left: 27px; top: 257px; display: flex; gap: 5px; }
  .dots span { width: 9px; height: 9px; border-radius: 50%; background: var(--brown); }

  /* welcome */
  .band-white { left: 0; width: 922px; background: var(--white); border-top: 1px solid var(--rule); border-bottom: 1px solid var(--rule); }
  .welcome h2 { position: absolute; left: 57px; top: 453px; }
  .welcome p { position: absolute; left: 57px; top: 478px; width: 463px; }
  .about { left: 541px; top: 422px; width: 324px; height: 216px; background: var(--brown); color: #f3e7df; overflow: hidden; }
  .about svg.diag { position: absolute; left: 0; top: 0; }
  .about h2 { position: absolute; left: 16px; top: 12px; color: var(--white); font-size: 14.5px; }
  .about .name { position: absolute; left: 16px; top: 36px; color: var(--white); font-size: 11.5px; }
  .about .name i { font-size: 7.5px; }
  .about p { position: absolute; left: 16px; top: 53px; width: 270px; font-size: 9px; line-height: 16.4px; white-space: nowrap; z-index: 1; }
  .about .btn { left: 16px; top: 168px; background: var(--white); color: var(--brown); }
  .portrait { left: 218px; top: 110px; width: 106px; height: 106px; background: linear-gradient(180deg, #8d8b86, #2f3442); }

  /* services / practice */
  .col h2 { position: absolute; top: 659px; }
  .lead { left: 57px; top: 685px; width: 380px; color: var(--brown); font-size: 10px; line-height: 14px; }
  .list { list-style: none; position: absolute; }
  .list li { height: 18.4px; line-height: 18.4px; padding-left: 18px; position: relative; font-size: 9.2px; }
  .list li svg { position: absolute; left: 0; top: 6px; }
  .statue { left: 718px; top: 662px; width: 147px; height: 246px; background: linear-gradient(90deg, #3b2320, #8a7f78 50%, #4a2a24); }

  /* news / blog */
  .news-col { position: absolute; top: 982px; width: 175px; }
  .news-col .date { color: #333; font-size: 9.6px; }
  .news-col p { margin-top: 2px; }
  .news-col .link { display: block; margin-top: 11px; }
  .blog-col { width: 186px; }
  .blog-col .title { color: #333; font-size: 10px; line-height: 14px; }
  .blog-col .meta { color: var(--brown); font-size: 8px; margin-top: 2px; }
  .blog-col p { font-size: 9px; line-height: 14.5px; }
  .divider { left: 452px; top: 956px; width: 1px; height: 148px; background: var(--rule); }

  /* footer */
  .legal { left: 57px; top: 1145px; font-size: 9.2px; line-height: 18px; color: #6b6460; }
  .legal .firm { color: var(--brown); }
  .social { left: 764px; top: 1152px; display: flex; gap: 6px; }
  .social span { display: flex; align-items: center; gap: 3px; font-size: 8.5px; color: var(--brown); }
  .social i { display: block; width: 8px; height: 8px; background: var(--brown); }
</style>
</head>
<body>

<header>
  <div class="abs brand">GERALD T. <b>CORVEY</b></div>
  <div class="abs contact phone">
    <svg width="14" height="14" viewBox="0 0 14 14"><rect width="14" height="14" rx="2" fill="#6f3d2c"/><path d="M4 3.5c1 0 1.5 2 1 2.5s-.5.8.5 2 1.6 1.5 2 1 2.5 0 2.5 1-1.5 1.5-2.5 1.2C5.5 10.5 3.5 8 3 6 2.8 4.7 3.2 3.5 4 3.5z" fill="#f8f3e8"/></svg>
    PHONE:<br><span class="value">617 555-0142</span>
  </div>
  <div class="abs contact email">
    <svg width="14" height="10" viewBox="0 0 14 10"><rect width="14" height="10" fill="#6f3d2c"/><path d="M0 0l7 5.5L14 0" stroke="#f8f3e8" fill="none" stroke-width="1.2"/></svg>
    EMAIL:<br><span class="value">gcorvey@mcorveyfirm.com</span>
  </div>
  <nav class="abs nav">
    <ul>
      <li class="active">HOME</li>
      <li>WHY HIRE ME?</li>
      <li>SUCCESS STORIES</li>
      <li>PRACTICE AREAS</li>
      <li>REPRESENTATIVE CLIENTS</li>
      <li>SERVICES PROVIDED</li>
      <li>CONTACT US</li>
      <li>HOW TO FIND US</li>
    </ul>
  </nav>
</header>

<section class="abs hero">
  <div class="hero-art" role="img" aria-label="Photo of business people shaking hands beside a large wooden gavel">
    <div class="abs hero-text">Protecting and Defending Your Business Against Competitors, Rogue Employees, Cheating Business Partners, Devious Contracting Parties, and Overzealous Government Agencies.</div>
    <div class="abs dots"><span></span><span></span><span></span><span></span></div>
  </div>
</section>

<section class="abs band-white welcome" style="top:432px;height:197px;"></section>
<section class="welcome">
  <h2>Welcome to our website</h2>
  <p>Aliquam molestie, mi et imperdiet euismod, dui purus auctor tellus, et interdum lacus lectus et ante. Sed accumsan sollicitudin sapien, sit amet adipiscing turpis gravida ac. In congue, neque ac lobortis volutpat, libero mauris varius mi, vitae suscipit ipsum ligula vitae risus. Duis aliquam nibh a dui iaculis viverra id a velit. Vivamus egestas risus in magna varius commodo. Sed semper viverra egestas. Etiam pretium porttitor lectus, vel ornare neque porta volutpat.</p>
  <a class="btn" style="left:57px;top:583px;">READ MORE ››</a>
</section>

<aside class="abs about">
  <svg class="diag" width="324" height="216"><polygon points="324,40 324,216 160,216" fill="#7c4a38"/></svg>
  <h2>About me</h2>
  <div class="name">Gerald T. Corvey <i>(Law Office of Gerald T. Corvey)</i></div>
  <p>Aliquam molestie, mi et imperdiet euismod, dui purus auctor<br>tellus, et interdum lacus lectus et ante. Sed accumsan<br>sollicitudin sapien, sit amet adipiscing turpis gravida ac.<br>In congue, neque ac lobortis volutpat, libero mauris<br>varius mi, vitae suscipit ipsum ligula vitae risus.<br>Duis aliquam nibh a dui iaculis viverra..</p>
  <a class="btn">READ MORE ››</a>
  <div class="abs portrait" role="img" aria-label="Portrait photo of the attorney"></div>
</aside>

<section class="col services">
  <h2 style="left:57px;">Services we provide</h2>
  <div class="abs lead">Providing all aspects of employment counseling, documenting and litigation,<br>including the following:</div>
  <ul class="list" style="left:57px;top:719px;">
    <li><svg width="10" height="6"><path d="M0 3h9M6 0l3 3-3 3" stroke="#6f3d2c" fill="none"/></svg>Defending and prosecuting lawsuits.</li>
    <li><svg width="10" height="6"><path d="M0 3h9M6 0l3 3-3 3" stroke="#6f3d2c" fill="none"/></svg>Defending MCAD and EEOC claims and other agency filings.</li>
    <li><svg width="10" height="6"><path d="M0 3h9M6 0l3 3-3 3" stroke="#6f3d2c" fill="none"/></svg>Drafting/modifying noncompete agreements.</li>
    <li><svg width="10" height="6"><path d="M0 3h9M6 0l3 3-3 3" stroke="#6f3d2c" fill="none"/></svg>Draft/review/modify employee handbooks.</li>
    <li><svg width="10" height="6"><path d="M0 3h9M6 0l3 3-3 3" stroke="#6f3d2c" fill="none"/></svg>Draft/review/modivy employment offer letters and contracts.</li>
    <li><svg width="10" height="6"><path d="M0 3h9M6 0l3 3-3 3" stroke="#6f3d2c" fill="none"/></svg>Consult on hiring and firing issues.</li>
    <li><svg width="10" height="6"><path d="M0 3h9M6 0l3 3-3 3" stroke="#6f3d2c" fill="none"/></svg>Consult on employee leave issues.</li>
    <li><svg width="10" height="6"><path d="M0 3h9M6 0l3 3-3 3" stroke="#6f3d2c" fill="none"/></svg>Consult on emploment practices and policies.</li>
  </ul>
  <a class="btn" style="left:57px;top:886px;">READ MORE ››</a>
</section>

<section class="col practice">
  <h2 style="left:472px;">Practice area</h2>
  <ul class="list" style="left:472px;top:683px;">
    <li><svg width="10" height="6"><path d="M0 3h9M6 0l3 3-3 3" stroke="#6f3d2c" fill="none"/></svg>Employment Counseling and Litigation</li>
    <li><svg width="10" height="6"><path d="M0 3h9M6 0l3 3-3 3" stroke="#6f3d2c" fill="none"/></svg>Hiring and Firing.</li>
    <li><svg width="10" height="6"><path d="M0 3h9M6 0l3 3-3 3" stroke="#6f3d2c" fill="none"/></svg>Wage and Hour Issues.</li>
    <li><svg width="10" height="6"><path d="M0 3h9M6 0l3 3-3 3" stroke="#6f3d2c" fill="none"/></svg>Noncompetes.</li>
    <li><svg width="10" height="6"><path d="M0 3h9M6 0l3 3-3 3" stroke="#6f3d2c" fill="none"/></svg>Sexual Harassment.</li>
    <li><svg width="10" height="6"><path d="M0 3h9M6 0l3 3-3 3" stroke="#6f3d2c" fill="none"/></svg>Leave Issues under the ADA, FMLA and State Law.</li>
    <li><svg width="10" height="6"><path d="M0 3h9M6 0l3 3-3 3" stroke="#6f3d2c" fill="none"/></svg>Business Litigation</li>
    <li><svg width="10" height="6"><path d="M0 3h9M6 0l3 3-3 3" stroke="#6f3d2c" fill="none"/></svg>Interference with Contractual Relations.</li>
    <li><svg width="10" height="6"><path d="M0 3h9M6 0l3 3-3 3" stroke="#6f3d2c" fill="none"/></svg>Breach of Contract.</li>
    <li><svg width="10" height="6"><path d="M0 3h9M6 0l3 3-3 3" stroke="#6f3d2c" fill="none"/></svg>Defamation (slander and lible).</li>
  </ul>
  <a class="btn" style="left:472px;top:886px;">READ MORE ››</a>
  <div class="abs statue" role="img" aria-label="Photo of a bronze statue of Lady Justice in front of law books"></div>
</section>

<section class="abs band-white" style="top:932px;height:196px;"></section>
<section class="news">
  <h2 class="abs" style="left:57px;top:953px;">Latest news</h2>
  <article class="news-col" style="left:57px;">
    <div class="date">AUG 04, 2014</div>
    <p>Aliquam molestie, mi et imperdiet euismod, dui purus auctor tellus, et interdum lacus lectus et ante. Sed accumsan sollicitudin sapien, sit amet adipiscing turpis gravida ac....</p>
    <a class="link">READ MORE ››</a>
  </article>
  <article class="news-col" style="left:266px;">
    <div class="date">AUG 04, 2014</div>
    <p>Aliquam molestie, mi et imperdiet euismod, dui purus auctor tellus, et interdum lacus lectus et ante. Sed accumsan sollicitudin sapien, sit amet adipiscing turpis gravida ac....</p>
    <a class="link">READ MORE ››</a>
  </article>
  <div class="abs divider"></div>
  <h2 class="abs" style="left:472px;top:953px;">Recent blog</h2>
  <article class="news-col blog-col" style="left:472px;">
    <div class="title">You're Damned If You Don't Respond Appropriately to a Poor Rateline Review or Online Post.</div>
    <div class="meta">Posted: January 15, 2014 in Lawsuits</div>
    <p>Pellentesque habitant morbi tristique senectus et netus et malesuada fames ac turpis egestas. Nunc consequat congue..</p>
    <a class="link">READ MORE ››</a>
  </article>
  <article class="news-col blog-col" style="left:681px;">
    <div class="title">You're Damned If You Don't Respond Appropriately to a Poor Rateline Review or Online Post.</div>
    <div class="meta">Posted: January 15, 2014 in Lawsuits</div>
    <p>Pellentesque habitant morbi tristique senectus et netus et malesuada fames ac turpis egestas. Nunc consequat congue..</p>
    <a class="link">READ MORE ››</a>
  </article>
</section>

<footer>
  <div class="abs legal">Copyright © 2014. <span class="firm">Law Office of Gerald T. Corvey</span><br>All Right Reserved &nbsp;|&nbsp; Term of Services</div>
  <div class="abs social">
    <span><i></i>Folio</span>
    <span><i></i>Chirper</span>
    <span><i></i>Linkwork</span>
  </div>
</footer>

</body>
</html>
```